Website for legal services (estates law) called KTV ESTATES LAW

Simple, catchy and easy to use. I am providing estates legal services and I want clients to feel a warm, friendly but professional vibe when they visit my website. I don't want harsh legal pictures (like a picture of a tough lawyer, or pictures of scales of justice). Pictures of books, plants, signing documents or a comfortable looking office are acceptable.

Please use wordpress to design it because I want ability to upload blogs on my own through wordpress after. I am attaching my logo.

Target Market(s)

Millenials, boomers, people in their 40's and anyone looking to transfer property titles or create a will, or anyone whose relatives have died and need help with estates administration.

Industry/Entity Type

Law Firm

Coding

Coded - Design and coding required

Number of Pages Required

4 page

Font styles to use
Sans Serif

Colors
0493ce
33a6d7
85cae6
cee9f5
f4fafd

Requirements
Must have
• - Must be designed with WordPress
- Must have a warm, friendly, professional vibe
- I want to be able to edit any of the content of the website myself
Nice to have
• Pictures of law books, plants, signing documents or a comfortable looking office are acceptable.
Should not have
• I don't want harsh legal pictures (like a picture of a tough lawyer, or pictures of scales of justice).

```html
<!DOCTYPE html>
<html lang="en">
<head>
<meta charset="utf-8">
<title>KTV Estates Law</title>
<link href="https://fonts.googleapis.com/css2?family=Raleway:wght@300;400;500;700;800&display=swap" rel="stylesheet">
<style>
:root{
  --teal:#0e9a86;
  --blue:#0493ce;
  --blue-light:#33a6d7;
  --ink:#2b2b2b;
  --text:#555;
  --grey-band:#a7a7aa;
  --dark:#3a3a3c;
  --white:#fff;
}
*{margin:0;padding:0;box-sizing:border-box}
html,body{width:1200px;height:3367px;overflow:hidden}
body{position:relative;font-family:"Raleway",sans-serif;color:var(--ink);background:var(--white)}
.abs{position:absolute}
.topbar{left:614px;top:0;width:586px;height:50px;background:var(--teal);clip-path:polygon(22px 0,100% 0,100% 100%,0 100%);color:#fff;font-size:15px;display:flex;align-items:center;gap:30px;padding-left:42px}
.topbar .phone{font-size:19px}
.topbar .social{margin-left:auto;margin-right:28px;display:flex;gap:8px}
.topbar .social span{width:9px;height:9px;border-radius:50%;background:#fff;display:block}
.brand{left:112px;top:52px;display:flex;align-items:center;gap:8px;font-weight:700;font-size:19px;color:var(--ink);letter-spacing:.5px}
.brand .mark{width:14px;height:14px;background:var(--ink)}
.nav{left:359px;top:82px;display:flex;gap:31px;font-size:15px;color:#333}
.nav .active{color:var(--teal)}
.btn{display:inline-flex;align-items:center;justify-content:center;border-radius:30px;color:#fff;background:var(--blue);font-size:15px;font-weight:500}
.nav-btn{left:935px;top:62px;width:154px;height:50px;box-shadow:0 0 0 3px #d5eef8}
.hero{left:0;top:119px;width:1200px;height:672px;background:linear-gradient(180deg,#3a2a20,#5a3a28 40%,#2a1f1a)}
.hero h1{left:110px;top:352px;font-size:57px;font-weight:800;color:#fff}
.hero-sub{left:110px;top:421px;width:460px;font-size:18px;line-height:30px;color:#fff}
.hero-btn{left:110px;top:497px;width:157px;height:45px}
.about-img1{left:112px;top:876px;width:340px;height:281px;background:linear-gradient(135deg,#d9dde2,#9aa3ab)}
.about-img2{left:226px;top:987px;width:336px;height:278px;background:linear-gradient(135deg,#e8e2d6,#8e8170);border:4px solid #fff;box-shadow:0 2px 6px rgba(0,0,0,.25)}
.dot{border-radius:50%}
.about h2{left:621px;top:866px;font-size:41px;font-weight:700}
.about-text{left:622px;top:925px;width:464px;font-size:15px;line-height:34.3px;color:var(--text);text-align:justify;font-weight:300}
.read-btn{left:616px;top:1212px;width:153px;height:49px}
.services-bg{left:0;top:1370px;width:1200px;height:1030px}
.services h2{left:0;top:1543px;width:1200px;text-align:center;font-size:41px;font-weight:700;color:#fff}
.svc-img{top:1621px;width:472px;height:355px}
.svc-col{top:2005px;width:472px;color:#fff}
.svc-col h3{font-size:20px;font-weight:500;margin-bottom:20px}
.svc-col li{list-style:none;position:relative;padding-left:22px;font-size:15px;line-height:30px;margin-bottom:10px}
.svc-col li::before{content:"";position:absolute;left:2px;top:10px;border-left:7px solid #7fd6c8;border-top:5px solid transparent;border-bottom:5px solid transparent}
.projects h2{left:0;top:2475px;width:1200px;text-align:center;font-size:41px;font-weight:700}
.proj{top:2541px;width:317px;height:299px}
.proj .cap{position:absolute;left:0;bottom:0;width:100%;height:48px;background:rgba(0,0,0,.45);color:#fff;font-size:15px;padding:14px 18px}
.proj-title{top:2866px;width:317px;text-align:center;font-size:15px}
.footer-bg{left:0;top:3020px;width:1200px;height:347px}
.fcol{top:3160px;width:360px;text-align:center;color:#fff;font-size:15px;line-height:27px}
.fcol .ico{width:52px;height:52px;border:1.5px solid #9ad9d0;border-radius:50%;margin:0 auto 14px;display:flex;align-items:center;justify-content:center}
.fcol h4{font-size:16px;font-weight:500;margin-bottom:6px}
.copy{left:0;top:3320px;width:1200px;text-align:center;color:#fff;font-size:14px}
</style>
</head>
<body>
<div class="abs topbar"><span class="phone">✆ 800-555-0199</span><span>hello@ktvlaw-example.com</span><span class="social"><span></span><span></span></span></div>
<div class="abs brand"><span class="mark"></span>KTV ESTATES LAW</div>
<nav class="abs nav"><span class="active">HOME</span><span>ABOUT</span><span>SERVICES</span><span>PROJECTS</span><span>BLOGS</span><span>CONTACT</span></nav>
<a class="abs btn nav-btn">TAKE ACTION</a>

<div class="abs hero" role="img" aria-label="Shelves of antique leather-bound law books"></div>
<svg class="abs" style="left:0;top:630px" width="1200" height="170" viewBox="0 0 1200 170">
  <polygon points="0,170 1200,20 1200,170" fill="#fff"/>
  <polygon points="145,165 1200,20 1200,30 145,162" fill="var(--grey-band)"/>
  <polygon points="140,150 1200,8 1200,40 140,165" fill="var(--grey-band)"/>
  <polygon points="780,90 1200,20 1200,165" fill="var(--teal)"/>
  <circle cx="600" cy="39" r="5" fill="none" stroke="var(--teal)" stroke-width="1.5"/>
  <line x1="600" y1="50" x2="600" y2="135" stroke="var(--teal)" stroke-width="3" stroke-dasharray="2 6"/>
  <path d="M595 135 L600 141 L605 135" fill="none" stroke="var(--teal)" stroke-width="1.5"/>
</svg>
<h1 class="abs hero-title" style="left:110px;top:352px;font-size:57px;font-weight:800;color:#fff">KTV ESTATES LAW</h1>
<p class="abs hero-sub">where I endeavor to earn your trust and provide you with high quality estates and real estate law services</p>
<a class="abs btn hero-btn">GET STARTED</a>

<section class="about">
  <div class="abs about-img1" role="img" aria-label="Office team reviewing documents"></div>
  <div class="abs about-img2" role="img" aria-label="Hands signing a document at a desk"></div>
  <span class="abs dot" style="left:505px;top:873px;width:26px;height:26px;background:var(--blue)"></span>
  <span class="abs dot" style="left:469px;top:957px;width:13px;height:13px;background:var(--teal)"></span>
  <span class="abs dot" style="left:549px;top:961px;width:7px;height:7px;background:var(--blue-light)"></span>
  <h2 class="abs">ABOUT</h2>
  <p class="abs about-text">My name is Kira T. Vance and I am an estates and real estate lawyer. I graduated from Northfield University Faculty of Law and my passion is estates law and real estate law. Prior to entering the legal profession, I obtained my CPA (Chartered Professional Accounting) designation and worked in business and management accounting for many years, where I developed a deeper understanding of money and finances. As a lawyer, I lean on this foundation frequently for the benefit of my clients.</p>
  <a class="abs btn read-btn">READ MORE</a>
</section>

<section class="services">
  <svg class="abs services-bg" viewBox="0 0 1200 1030" preserveAspectRatio="none">
    <polygon points="0,6 1200,14 1200,830 0,1025" fill="var(--teal)"/>
    <polygon points="0,6 420,105 0,170" fill="var(--blue)"/>
    <polygon points="0,165 1020,22 1020,40 0,190" fill="var(--grey-band)"/>
  </svg>
  <h2 class="abs">OUR SERVICES</h2>
  <div class="abs svc-img" style="left:112px;background:linear-gradient(135deg,#e9e4dc,#6f5a48)" role="img" aria-label="Client pointing at a will while lawyer writes"></div>
  <div class="abs svc-img" style="left:618px;background:linear-gradient(135deg,#d9d6cf,#7a8a96)" role="img" aria-label="House keys handed over across a desk"></div>
  <div class="abs svc-col" style="left:112px"><h3>ESTATES LAW</h3><ul>
    <li>Wills (personal, corporate, foreign property)</li><li>Trusts</li>
    <li>Powers of Attorney for Personal Care and Property</li>
    <li>Asset planning to minimize income tax and estate administration tax upon your passing.</li></ul></div>
  <div class="abs svc-col" style="left:618px"><h3>REAL ESTATE LAW</h3><ul>
    <li>Transfers of title to family members or spouses</li>
    <li>Transfers of title from deceased to survivors;</li>
    <li>Transfers of title to estate trustee for the purposes of selling the estate's real estate asset.</li></ul></div>
</section>

<section class="projects">
  <h2 class="abs">OUR PROJECTS</h2>
  <svg class="abs" style="left:74px;top:2698px" width="14" height="24"><path d="M12 2 L2 12 L12 22" fill="none" stroke="#333" stroke-width="1.5"/></svg>
  <svg class="abs" style="left:1110px;top:2698px" width="14" height="24"><path d="M2 2 L12 12 L2 22" fill="none" stroke="#333" stroke-width="1.5"/></svg>
  <div class="abs proj" style="left:112px;background:linear-gradient(135deg,#c48a4e,#3a2414)" role="img" aria-label="Stack of old leather books"><div class="cap">Lorem ipsum dolor sit</div></div>
  <div class="abs proj" style="left:442px;background:linear-gradient(135deg,#e5e7e9,#8a8f94)" role="img" aria-label="Small house model on a desk with contract"><div class="cap">Lorem ipsum dolor sit</div></div>
  <div class="abs proj" style="left:772px;background:linear-gradient(135deg,#5f6d7a,#d8dde2)" role="img" aria-label="Businessman reviewing a document"><div class="cap">Lorem ipsum dolor sit</div></div>
  <div class="abs proj-title" style="left:112px">LOREM IPSUM DOLOR SIT</div>
  <div class="abs proj-title" style="left:442px">LOREM IPSUM DOLOR SIT</div>
  <div class="abs proj-title" style="left:772px">LOREM IPSUM DOLOR SIT</div>
</section>

<footer>
  <svg class="abs footer-bg" viewBox="0 0 1200 347" preserveAspectRatio="none">
    <polygon points="0,24 145,0 1200,100 1200,347 0,347" fill="var(--dark)"/>
    <polygon points="145,4 1200,88 1200,110 145,22" fill="var(--grey-band)"/>
    <polygon points="940,84 1200,0 1200,98" fill="var(--teal)"/>
  </svg>
  <div class="abs fcol" style="left:53px"><div class="ico"><svg width="20" height="20" viewBox="0 0 24 24"><path d="M6 3l3 4-2 2c1 3 4 6 7 7l2-2 4 3-2 4C10 21 3 14 3 5z" fill="none" stroke="#9ad9d0" stroke-width="1.5"/></svg></div><h4>PHONE</h4>Telephone - 555.014.2280<br>Fax - 555.014.2281</div>
  <div class="abs fcol" style="left:407px"><div class="ico"><svg width="18" height="22" viewBox="0 0 18 22"><path d="M9 21C4 14 2 11 2 8a7 7 0 0114 0c0 3-2 6-7 13z" fill="var(--teal)"/><circle cx="9" cy="8" r="2.5" fill="var(--dark)"/></svg></div><h4>ADDRESS</h4>1200 Harbour Lane, Suite 410,<br>Lakeview ON L0A1B2</div>
  <div class="abs fcol" style="left:770px"><div class="ico"><svg width="20" height="14" viewBox="0 0 20 14"><rect x="1" y="1" width="18" height="12" fill="none" stroke="#9ad9d0" stroke-width="1.5"/><path d="M1 1l9 7 9-7" fill="none" stroke="#9ad9d0" stroke-width="1.5"/></svg></div><h4>EMAIL</h4>kira@ktvlaw-example.ca<br>www.ktvlaw-example.ca</div>
  <div class="abs copy">© 2020 All Rights Reserved</div>
</footer>
</body>
</html>
```